Speisekarten für griechisches Restaurant
Zielgruppe
modernes griechisches Restaurant
Aufgabenstellung
neues modernen helles design ,
nach Durchsicht aus meinen Vorlangen, sollten ein paar Anpassung am text und preisen noch durchgeführt werden.
aus der pdf datei,, ist ab Seite 7 die richtige Speisekarte,, vorher sind nur entwürfe vom mir, diese bitte ignorieren.

```html
<!DOCTYPE html>
<html lang="de">
<head>
<meta charset="utf-8">
<title>Speisekarte – Griechisches Restaurant</title>
<link href="https://fonts.googleapis.com/css2?family=Oswald:wght@600&family=Work+Sans:ital,wght@0,400;0,500;1,400&display=swap" rel="stylesheet">
<style>
:root{
  --canvas:#ffffff;
  --paper:#f0efed;
  --ink:#1d1d1b;
  --muted:#55544f;
  --gold:#b2a377;
  --gold-text:#c2a96a;
  --rule:#3a3a38;
}
*{box-sizing:border-box;margin:0;padding:0}
html,body{width:893px;height:1200px;overflow:hidden;background:var(--canvas)}
body{position:relative;font-family:"Work Sans",Arial,sans-serif;color:var(--ink)}
.page{position:absolute;width:379px;height:537px;background:var(--paper);box-shadow:4px 4px 6px rgba(0,0,0,.28)}
.p1{left:59px;top:50px}.p2{left:455px;top:50px}.p3{left:59px;top:615px}.p4{left:455px;top:615px}
.footer{position:absolute;left:0;right:0;bottom:0;height:23px;background:var(--gold);color:#e9e2cc;font-size:4.5px;font-style:italic;padding:8px 0 0 113px}
.p4 .footer,.p2 .footer{padding-left:107px}
.spine{position:absolute;left:78px;top:40px;width:1px;height:482px;background:var(--rule)}
.p2 .spine{left:72px;top:45px;height:465px}
.p3 .spine{top:38px;height:442px}
.p4 .spine{top:40px;height:485px}
.title{position:absolute;font-family:"Oswald",Arial,sans-serif;font-weight:600;font-size:19px;letter-spacing:.2px;transform:rotate(-90deg);transform-origin:left top;white-space:nowrap;line-height:1}
.p1 .title{left:61px;top:202px}.p2 .title{left:56px;top:212px}.p3 .title{left:61px;top:142px}
.col{position:absolute;left:113px;width:200px}
.p2 .col,.p4 .col{left:107px}
.note{color:var(--gold-text);font-style:italic;font-size:5.6px;line-height:1.55}
h2{font-size:7.6px;font-weight:500;letter-spacing:.3px;padding-bottom:6px;border-bottom:1px solid var(--rule)}
.dish{position:relative;padding-left:0;margin-top:9px}
.dish .num{position:absolute;left:-13px;top:0;color:var(--gold-text);font-size:7px}
.dish .name{font-size:7.6px;font-weight:500;letter-spacing:.2px;line-height:1.2}
.dish .desc{font-size:5.8px;color:var(--muted);line-height:1.4}
.dish .price{position:absolute;right:12px;top:0;font-size:6.6px;color:var(--muted)}
sup{font-size:3.6px}
.divider{height:1px;background:var(--rule);margin-top:10px}
.drink{display:flex;align-items:baseline;font-size:7.6px;font-weight:500;letter-spacing:.2px;line-height:1.45}
.drink .n{flex:1}
.drink .q{font-size:4.6px;font-style:italic;color:var(--gold-text);font-weight:400;width:auto;margin-left:6px}
.drink .v{font-size:6.4px;color:var(--muted);font-weight:400;width:20px;text-align:right}
.drink .light{font-weight:400}
.sub{font-size:5.8px;color:var(--muted);line-height:1.4;margin-bottom:1px}
.section{margin-top:10px}
.section h2{margin-bottom:7px}
.spirits .drink{line-height:1.7}
</style>
</head>
<body>

<section class="page p1">
  <div class="spine"></div>
  <div class="title">SUPPEN &amp; SALATE</div>
  <div class="col" style="top:68px">
    <p class="note">Alle unsere hausgemachten Suppen und Salate<br>werden mit Brot begleitet</p>
    <h2 style="margin-top:30px">SUPPEN</h2>
    <div class="dish"><span class="num">29</span><div class="name">KREMIDOSOUPA ⓥ</div><div class="desc">Zwiebelsuppe mit Käse<sup>1</sup> überbacken</div><span class="price">6.50</span></div>
    <div class="dish"><span class="num">30</span><div class="name">KOTOSOUPA</div><div class="desc">Hausgemachte Hühnersuppe</div><span class="price">6.50</span></div>
    <h2 style="margin-top:62px">SALATE</h2>
    <div class="dish"><span class="num">33</span><div class="name">BEILAGEN SALAT ⓥ</div><div class="desc">Mixsalat mit Hausdressing<sup>2,4,6,C,I,J</sup></div><span class="price">5.00</span></div>
    <div class="dish"><span class="num">34</span><div class="name">CHORIATIKI ⓥ</div><div class="desc">Griechischer Bauernsalat mit Olivenöl<sup>7,F</sup></div><span class="price">13.50</span></div>
    <div class="dish"><span class="num">36</span><div class="name">SALATA TONNOS ⓥ</div><div class="desc">Mixsalat mit Thunfisch<sup>D</sup> in Balsamico-Dressing<sup>1,3,6</sup></div><span class="price">13.50</span></div>
    <div class="dish"><span class="num">38</span><div class="name">SALATA GAVROS</div><div class="desc">Mixsalat mit Sardellen<sup>D</sup> in Balsamico-Dressing<sup>1,3,6</sup></div><span class="price">15.00</span></div>
    <div class="dish"><span class="num">39</span><div class="name">ANTI-STRESS</div><div class="desc">Mixsalat mit Putenstreifen in Balsamico-Dressing<sup>1,3,6</sup></div><span class="price">15.00</span></div>
    <div class="dish"><span class="num">40</span><div class="name">SALATA GARIDAS</div><div class="desc">Mixsalat mit Gambas<sup>B</sup> in Balsamico-Dressing<sup>1,3,6</sup></div><span class="price">15.00</span></div>
  </div>
  <div class="footer">Menü-Änderungen mit Mehraufwand werden mit einem Aufpreis berechnet.</div>
</section>

<section class="page p2">
  <div class="spine"></div>
  <div class="title">PFANNENGERICHTE</div>
  <div class="col" style="top:63px;width:212px">
    <p class="note">Tiganiá ist ein traditionelles griechisches Gericht,<br>das aus Fleisch, Gemüse und einer Sauce besteht</p>
    <div class="divider" style="margin-top:14px"></div>
    <p class="note" style="margin-top:14px">Diese Gerichte werden mit<br>Salat und Patatakia serviert</p>
    <div class="dish" style="margin-left:12px;margin-top:10px"><span class="num">43</span><div class="name">AETOS</div><div class="desc">Schweinefilet-Medaillons mit frischen<br>Champignons und Sauce nach Wahl:<br>Brandy/ Pfeffer <sup>F,4,A,C,F,G,I,J</sup><br>Pikante Sauce <sup>F,4,A,C,F,G,I,J</sup> verfeinert mit Weißwein</div><span class="price">22.00</span></div>
    <div class="dish" style="margin-left:12px"><span class="num">44</span><div class="name">CHEF</div><div class="desc">Verschiedene Fleischsorten in einer<br>Tomaten-Knoblauch-Sauce mit<br>Crème-Fraîche verfeinert <sup>F</sup></div><span class="price">22.50</span></div>
    <div class="dish" style="margin-left:12px"><span class="num">45</span><div class="name">SKORDO</div><div class="desc">Verschiedene Fleischsorten mit<br>Knoblauch, Paprika, Zwiebeln<br>und Fetakäse <sup>F</sup></div><span class="price">22.50</span></div>
    <div class="divider" style="margin-top:18px"></div>
    <p class="note" style="margin-top:16px">Diese Gerichte werden mit<br>Salat und Reis serviert</p>
    <div class="dish" style="margin-left:12px;margin-top:10px"><span class="num">46</span><div class="name">GALAPOULA</div><div class="desc">Putengeschnetzeltes mit frischen<br>Champignons, verfeinert mit einer<br>pikanten Sauce <sup>F,4,A,C,F,G,I,J</sup></div><span class="price">21.50</span></div>
    <div class="dish" style="margin-left:12px"><span class="num">47</span><div class="name">MON AMOUR</div><div class="desc">Hähnchenbrustfilet in einer<br>Spezial-Fetasauce <sup>F</sup></div><span class="price">21.00</span></div>
    <div class="dish" style="margin-left:12px"><span class="num">48</span><div class="name">NAXOS</div><div class="desc">Rumpsteak- Schweine- Putenfilet in<br>Spezial-Fetasauce mit Zucchini<br>und Auberginenwürfel <sup>F</sup></div><span class="price">24.00</span></div>
  </div>
  <div class="footer">Alle Preise sind in Euro angegeben.</div>
</section>

<section class="page p3">
  <div class="spine"></div>
  <div class="title">GETRÄNKE</div>
  <div class="col" style="top:60px">
    <div class="drink"><span class="n">STILLES WASSER</span><span class="q">Fl. 0,25 l</span><span class="v">2.80</span><span class="q">Fl. 0,75 l</span><span class="v">6.00</span></div>
    <div class="drink"><span class="n">MINERALWASSER</span><span class="q">Fl. 0,25 l</span><span class="v">2.80</span><span class="q">Fl. 0,75 l</span><span class="v">6.00</span></div>
    <div class="drink"><span class="n">FRUCHTSÄFTE</span><span class="q">Fl. 0,20 l</span><span class="v">2.00</span></div>
    <div class="sub">Orangensaft, Apfelsaft,<br>Kirschensaft, Traubensaft</div>
    <div class="drink"><span class="n">LIMONADEN</span></div>
    <div class="drink"><span class="n light" style="font-size:6px">KOLA CLASSIC <sup>2,3</sup>, ZERO <sup>2,3</sup>, ORANGENLIMO <sup>1</sup></span><span class="q">0,30 l</span><span class="v">3.00</span><span class="q">0,50 l</span><span class="v">4.50</span></div>
    <div class="sub" style="text-transform:uppercase;font-size:5.6px">Zitronenlimo <sup>4</sup>, Mischlimo <sup>1,5</sup>, Apfelschorle</div>
    <div class="drink"><span class="n light" style="font-size:6px">TONICWERK: Bitter Lemon,</span><span class="q">Fl. 0,20 l</span><span class="v">3.00</span></div>
    <div class="sub">Tonic, Ginger Ale</div>
    <div class="section"><h2>WARME GETRÄNKE</h2>
      <div class="drink"><span class="n">MOCCA <sup>8</sup></span><span class="v">3.00</span></div>
      <div class="drink"><span class="n">ESPRESSO <sup>8</sup></span><span class="v">2.60</span></div>
      <div class="drink"><span class="n">DOP. ESPRESSO <sup>8</sup></span><span class="v">3.50</span></div>
      <div class="drink"><span class="n">LATTE MACCHIATO <sup>8,F</sup></span><span class="v">4.00</span></div>
      <div class="drink"><span class="n">CAPPUCCINO <sup>8,F</sup></span><span class="v">3.50</span></div>
      <div class="drink"><span class="n">KAFFEE <sup>8</sup></span><span class="v">2.80</span></div>
      <div class="drink"><span class="n">TEE</span><span class="v">2.50</span></div>
    </div>
    <div class="section"><h2>BIER VOM FASS</h2>
      <div class="drink"><span class="n">HÜGEL PILSENER <sup>1,A</sup></span><span class="q">0,30 l</span><span class="v">3.20</span><span class="q">0,40 l</span><span class="v">4.00</span></div>
      <div class="drink"><span class="n">ALSTER RADLER</span><span class="q">0,30 l</span><span class="v">3.20</span><span class="q">0,40 l</span><span class="v">4.00</span></div>
      <div class="drink"><span class="n">THALASSA</span><span class="q">0,30 l</span><span class="v">3.50</span></div>
      <div class="drink"><span class="n">RHEINUFER ALT</span><span class="q">0,30 l</span><span class="v">3.20</span><span class="q">0,40 l</span><span class="v">4.00</span></div>
      <div class="drink"><span class="n">ALT - SCHUSS <sup>3</sup></span><span class="q">0,30 l</span><span class="v">3.20</span><span class="q">0,40 l</span><span class="v">4.00</span></div>
    </div>
    <div class="section"><h2>WEIZENBIER</h2>
      <div class="drink"><span class="n">TALHOF <sup>A</sup></span><span class="q">Fl. 0,50 l</span><span class="v">4.50</span></div>
      <div class="drink"><span class="n">TALHOF <sup>A</sup> <span class="light">Alkoholfrei</span></span><span class="q">Fl. 0,50 l</span><span class="v">4.50</span></div>
    </div>
    <div class="section"><h2>ALKOHOLFREIES BIER</h2>
      <div class="drink"><span class="n">WALDQUELL PILS</span><span class="q">Fl. 0,33 l</span><span class="v">4.50</span></div>
      <div class="drink"><span class="n">RHEINUFER ALT</span><span class="q">Fl. 0,33 l</span><span class="v">4.50</span></div>
      <div class="drink"><span class="n">MALZBIER</span><span class="q">Fl. 0,33 l</span><span class="v">3.00</span></div>
    </div>
  </div>
  <div class="footer">Menü-Änderungen mit Mehraufwand werden mit einem Aufpreis berechnet.</div>
</section>

<section class="page p4">
  <div class="spine"></div>
  <div class="col spirits" style="top:60px">
    <h2 style="margin-bottom:6px">SPIRITUOSEN</h2>
    <div class="drink"><span class="n">ARANCIO SPRITZ</span><span class="q">0,2 l</span><span class="v">6.50</span></div>
    <div class="drink"><span class="n">HUGO</span><span class="q">0,2 l</span><span class="v">6.50</span></div>
    <div class="drink"><span class="n">VERMUT BIANCO</span><span class="q">0,1 l</span><span class="v">5.00</span></div>
    <div class="drink"><span class="n">ROSSO AMARO ORANGE</span><span class="q">0,1 l</span><span class="v">5.00</span></div>
    <div class="drink" style="line-height:1.2"><span class="n">LONGDRINKS</span><span class="q">0,2 l</span><span class="v">5.00</span></div>
    <div class="sub">Vodka, Whiskey, Rum (4cl)<br>+ Mischgetränk</div>
    <div class="drink" style="line-height:1.2"><span class="n">NIKOS´ SCHNAPS KORB</span><span class="q">0,2 cl</span><span class="v">3.50</span></div>
    <div class="sub">Verschiedene exklusive Liköre<br>und Spirituosen aus Griechenland</div>
    <p class="note">Gerne beraten wir Sie bei der Auswahl</p>
    <div class="drink"><span class="n">OUZO</span><span class="q">0,2 cl</span><span class="v">2.50</span></div>
    <div class="drink"><span class="n">OUZO LESVOS</span><span class="q">Fl. 0,2 l</span><span class="v">14.00</span></div>
    <div class="drink"><span class="n">TSIPOURO (mit Anis)</span><span class="q">0,2 cl</span><span class="v">3.50</span></div>
    <div class="drink"><span class="n">TSIPOURO (mit Anis)</span><span class="q">0,2 cl</span><span class="v">3.50</span></div>
    <div class="drink"><span class="n">AETOS 5*</span><span class="q">0,2 cl</span><span class="v">4.00</span></div>
    <div class="drink"><span class="n">AETOS 7*</span><span class="q">0,2 cl</span><span class="v">5.00</span></div>
    <div class="drink"><span class="n">AETOS 40 JAHRE</span><span class="q">0,2 cl</span><span class="v">7.00</span></div>
    <div class="drink"><span class="n">AETOS FLAMBIERT</span><span class="q">0,2 cl</span><span class="v">7.00</span></div>
    <div class="drink"><span class="n">KRÄUTERBITTER</span><span class="q">0,2 cl</span><span class="v">3.00</span></div>
    <div class="drink"><span class="n">AMARO SICILIANO</span><span class="q">0,2 cl</span><span class="v">3.00</span></div>
    <div class="drink"><span class="n">FERNET ALPINO</span><span class="q">0,2 cl</span><span class="v">3.00</span></div>
    <div class="drink"><span class="n">NORDLYS AQUAVIT</span><span class="q">0,2 cl</span><span class="v">3.00</span></div>
    <div class="drink"><span class="n">JAGDHORN KRÄUTER</span><span class="q">0,2 cl</span><span class="v">3.00</span></div>
    <div class="drink"><span class="n">WILLIAMS CHRIST</span><span class="q">0,2 cl</span><span class="v">3.00</span></div>
    <div class="drink"><span class="n">TRESTERBRAND</span><span class="q">0,2 cl</span><span class="v">3.00</span></div>
    <div class="drink"><span class="n">IRISH CREAM</span><span class="q">0,2 cl</span><span class="v">3.00</span></div>
    <div class="drink"><span class="n">SAMBUCA</span><span class="q">0,2 cl</span><span class="v">3.00</span></div>
    <div class="drink"><span class="n">TEQUILA</span><span class="q">0,2 cl</span><span class="v">3.00</span></div>
    <div class="drink"><span class="n">LECKERCHEN</span><span class="q">0,2 cl</span><span class="v">2.30</span></div>
    <div class="drink"><span class="n">KUMQUAT - LIKÖR</span><span class="q">0,2 cl</span><span class="v">3.00</span></div>
    <div class="drink"><span class="n">BANANEN - LIKÖR</span><span class="q">0,2 cl</span><span class="v">3.00</span></div>
    <div class="drink"><span class="n">MASTICHA - LIKÖR</span><span class="q">0,2 cl</span><span class="v">3.00</span></div>
  </div>
  <div class="footer">Alle Preise sind in Euro angegeben.</div>
</section>

</body>
</html>
```